Brantley Advisory Group provides support for renewable energy projects to utilities and suppliers

I need a professional looking business card that is both simple and elegant and unique. My clients are mostly large organizations not individuals. I am a consultant with my own company that is small but would like to give clients the impression I am larger. Smart grid, fiber optics, software, field hardware, distribution automation, substation automation, operations, energy storage/batteries, microgrids, customer service, strategy/roadmaps, conservation, Automated Metering Infrastruture (AMI or smart meters) are all areas of focus.

Target Market(s)

Utilities, suppliers, governmental agencies involved in energy. All types of energy especially natural gas and electrical. Especially renewable energy or green projects.

Contact Information for Business Card

Name - Ross Brantley Cell Phone - 425.318.4762 Email - rbrantley@brantleyag-example.com
Company - Brantley Advisory Group (logo) Title - Principal

Font styles to use
Serif
Sans Serif

Colors

Designer to choose colors to be used in the design.

Requirements
Must have
• Simple and professional and powerful.
• Unique/creative design.
Nice to have
• Utilize color scheme to accent logo colors. Maybe some geometric pattern on edge of card with color.
Should not have
• Busy, complicated, traditional

```html
<!DOCTYPE html>
<html lang="en">
<head>
<meta charset="UTF-8">
<title>Brantley Advisory Group – Business Card</title>
<link href="https://fonts.googleapis.com/css2?family=Nunito:wght@700&family=Open+Sans:wght@400;700&display=swap" rel="stylesheet">
<style>
  :root {
    --backdrop: #2a2a2a;
    --card-blue: #1212a4;
    --brand-green: #5f9a34;
    --accent-lime: #a8e070;
    --paper: #ffffff;
    --ink-blue: #1515a0;
    --ink-grey: #6f6f6f;
  }
  * { box-sizing: border-box; margin: 0; padding: 0; }
  html, body { width: 1200px; height: 900px; overflow: hidden; }
  body {
    background: var(--backdrop);
    display: flex;
    flex-direction: column;
    align-items: center;
    justify-content: center;
    gap: 40px;
  }
  .card {
    width: 640px;
    height: 366px;
    position: relative;
    overflow: hidden;
  }

  /* Front */
  .card-front { background: var(--card-blue); }
  .brand {
    position: absolute;
    left: 70px;
    top: 130px;
    display: flex;
    align-items: center;
    gap: 16px;
  }
  .brand-square {
    width: 34px;
    height: 34px;
    border: 4px solid var(--paper);
    border-radius: 4px;
  }
  .brand-name {
    font-family: "Nunito", sans-serif;
    font-weight: 700;
    color: var(--paper);
    font-size: 28px;
    line-height: 1.15;
  }
  .pattern-area {
    position: absolute;
    right: 0;
    top: 40px;
    width: 250px;
    height: 300px;
    border-radius: 6px 0 0 6px;
    background: linear-gradient(135deg, #2a2ae0 0%, #6fa845 45%, #d9dce2 60%, #7fbf4e 78%, #2424d0 100%);
  }

  /* Back */
  .card-back { background: var(--paper); }
  .contact-block {
    position: absolute;
    left: 0;
    right: 0;
    top: 150px;
    display: flex;
    justify-content: center;
    align-items: center;
    gap: 22px;
    font-family: "Open Sans", sans-serif;
  }
  .identity { text-align: right; }
  .person-name {
    color: var(--ink-blue);
    font-weight: 700;
    font-size: 27px;
    line-height: 1.05;
    letter-spacing: 0.3px;
  }
  .person-title {
    color: var(--ink-grey);
    font-size: 17px;
  }
  .divider {
    width: 2px;
    height: 80px;
    background: var(--brand-green);
  }
  .details { list-style: none; }
  .details li {
    display: flex;
    align-items: center;
    gap: 10px;
    color: var(--ink-grey);
    font-size: 16px;
    line-height: 1.5;
  }
  .details svg { width: 18px; height: 18px; flex-shrink: 0; }
</style>
</head>
<body>

  <section class="card card-front">
    <div class="brand">
      <div class="brand-square"></div>
      <div class="brand-name">Brantley<br>Advisory Group</div>
    </div>
    <div class="pattern-area" role="img" aria-label="Decorative cluster of overlapping blue, green and silver squares"></div>
  </section>

  <section class="card card-back">
    <div class="contact-block">
      <div class="identity">
        <p class="person-name">ROSS BRANTLEY</p>
        <p class="person-title">Principal</p>
      </div>
      <div class="divider"></div>
      <ul class="details">
        <li>
          <svg viewBox="0 0 24 24" fill="none" stroke="#5f9a34" stroke-width="2" stroke-linecap="round" stroke-linejoin="round" aria-hidden="true">
            <path d="M22 16.9v3a2 2 0 0 1-2.2 2 19.8 19.8 0 0 1-8.6-3.1 19.5 19.5 0 0 1-6-6A19.8 19.8 0 0 1 2.1 4.2 2 2 0 0 1 4.1 2h3a2 2 0 0 1 2 1.7c.1 1 .4 1.9.7 2.8a2 2 0 0 1-.5 2.1L8 9.9a16 16 0 0 0 6 6l1.3-1.3a2 2 0 0 1 2.1-.4c.9.3 1.8.6 2.8.7a2 2 0 0 1 1.8 2z"/>
          </svg>
          425.318.4762
        </li>
        <li>
          <svg viewBox="0 0 24 24" fill="none" stroke="#5f9a34" stroke-width="2" stroke-linejoin="round" aria-hidden="true">
            <rect x="2" y="5" width="20" height="14" rx="1"/>
            <path d="M2 6l10 7 10-7"/>
          </svg>
          rbrantley@brantleyag-example.com
        </li>
      </ul>
    </div>
  </section>

</body>
</html>
```